SALT PAN COMPUTERS AD DESIGN

This is to go into our local phone book as a full page (A4) advert.

NOTE THAT THE DEADLINE IS MIDNIGHT SUNDAY THE 29TH AUSSIE WA TIME NOT THE ADVERTISED DEADLINE AS FOR THE LIFE OF ME I CANT SEE WHERE TO CHANGE IT.

HAPPY TO PAY EXTRA FOR A "YES THATS IT" JOB.

Title - SALT PAN COMPUTERS

(THINGS TO HAVE)
24/7 FULL COMPUTER SERVICES
ALL COMPUTER PROBLEMS SOLVED
info@saltpancomputers.com.au
0400 13 8562
SALTPANCOMPUTERS.COM.AU
Virus's Removed
Data Recovery
Custom Computers and Programs built
Picked up & Dropped off
Private and Business Welcome

Maybe this photo - http://www.pixelvaultlib.com/stock-photo-22810457-attractive-receptionist.php?st=a3e91f2
with 24/7 service.

http://www.pixelvaultlib.com/stock-photo-22936104-hard-disk-drive-service.php?st=7d2f5e8 with Data Recovery

http://www.pixelvaultlib.com/stock-illustration-5318890-laptop.php?st=e14b7c9

I don't know but I have less than 40 hours to do this...

Been extented for another 50 hours cause they stuffed up also I have just opened a logo one as well.

Reason: As the publisher stuffed up with my account I now have an extra 50 hours !!

please note increased payment, this may increase again.

Reason: Not ment to finish for another 18 hours !!!!!!

Keep Going !!!!

only 5 hours left before it has to be at the printers !!!!

• only have 40 hours left from now. it must be in by 7am Monday 30th western aussie time. (not eastern aussie time)
• A 3D look
Colors like dark blue, bright yellow black and dark red.
modern look
modern font ie..HandelGothicBT etc

```html
<!DOCTYPE html>
<html lang="en">
<head>
<meta charset="utf-8">
<title>Salt Pan Computers – Full Page Advert</title>
<link rel="stylesheet" href="https://fonts.googleapis.com/css2?family=Russo+One&family=Michroma&display=swap">
<style>
  :root {
    --navy: #06145a;
    --deep: #020a3a;
    --blue: #1b2fb0;
    --royal: #2c3fd0;
    --cyan: #2ec4ff;
    --yellow: #ffe600;
    --red: #e3101c;
    --steel: #b9bcc2;
    --steel-dark: #7d8087;
    --white: #ffffff;
    --ink: #000000;
  }
  * { margin: 0; padding: 0; box-sizing: border-box; }
  html, body { width: 848px; height: 1200px; overflow: hidden; background: var(--steel); }
  .advert {
    position: relative; width: 848px; height: 1200px; overflow: hidden;
    background: linear-gradient(180deg, #d0d2d6, var(--steel));
    font-family: "Russo One", "Arial Black", sans-serif;
  }
  .abs { position: absolute; }

  /* frame bars */
  .top-rail { left: 0; top: 0; width: 848px; height: 22px; background: linear-gradient(#e4e5e8, var(--steel-dark)); }
  .top-tab { left: 490px; top: 22px; width: 255px; height: 14px; background: var(--yellow); clip-path: polygon(0 0,100% 0,95% 100%,5% 100%); }
  .header {
    left: 0; top: 22px; width: 848px; height: 240px;
    background: radial-gradient(ellipse at 70% 40%, #1c3bc4 0%, var(--navy) 55%, var(--deep) 100%);
  }
  .logo-word { left: 163px; top: 88px; font-size: 52px; color: var(--yellow); letter-spacing: 1px; text-shadow: 2px 2px 0 var(--ink); }
  .header-rule { left: 38px; top: 194px; width: 480px; height: 1px; background: rgba(255,255,255,.6); }
  .tagline { left: 38px; top: 208px; font-size: 26px; color: var(--yellow); letter-spacing: -.5px; text-shadow: 2px 2px 0 var(--ink); }
  .header-band { left: 0; top: 258px; width: 848px; height: 36px; background: linear-gradient(180deg, #0a2aa8, var(--cyan) 45%, #0a2aa8); }
  .mid-rail { left: 0; top: 294px; width: 848px; height: 18px; background: linear-gradient(#e4e5e8, var(--steel-dark)); }

  /* main */
  .tech-art { left: 0; top: 312px; width: 474px; height: 556px; background: radial-gradient(circle at 55% 45%, #2a6fe0 0%, #0b2a8c 45%, var(--deep) 100%); }
  .services-panel {
    left: 478px; top: 312px; width: 370px; height: 556px;
    background: radial-gradient(ellipse at 55% 60%, var(--royal) 0%, var(--blue) 50%, #0d1a86 100%);
    border-left: 3px solid var(--cyan);
  }
  .services { position: absolute; right: 36px; top: 90px; list-style: none; text-align: right; }
  .services li { font-size: 30px; line-height: 35px; color: var(--yellow); text-shadow: 2px 2px 0 var(--ink); margin-bottom: 16px; letter-spacing: -.5px; }
  .services li span.arrow { color: var(--white); margin-right: 6px; }
  .laptop-art { left: 432px; top: 62px; width: 394px; height: 312px; background: linear-gradient(160deg, #f4f5f7, #9ea2a9); border-radius: 12px; }
  .laptop-small-art { left: 456px; top: 770px; width: 146px; height: 114px; background: linear-gradient(160deg, #eceef1, #8f939a); border-radius: 6px; }

  .badge {
    left: 20px; top: 580px; width: 306px; height: 306px; border-radius: 50%;
    background: radial-gradient(circle at 40% 35%, #fff7a0 0%, var(--yellow) 35%, #e9b800 100%);
    border: 3px solid #f6e9a0; box-shadow: 0 6px 18px rgba(0,0,0,.6);
    display: flex; align-items: center; justify-content: center; text-align: center;
    color: var(--red); font-size: 44px; line-height: 43px; letter-spacing: -1px;
  }

  /* contact strip */
  .contact-strip { left: 0; top: 868px; width: 848px; height: 208px; background: linear-gradient(180deg, #0b1e8e, var(--deep)); }
  .hdd-art { left: 0; top: 868px; width: 296px; height: 208px; background: radial-gradient(circle at 40% 50%, #c9d4ff 0%, #5b74d8 40%, #0f2282 100%); }
  .receptionist-art { left: 628px; top: 830px; width: 220px; height: 246px; background: radial-gradient(ellipse at 55% 40%, #f3d9a2 0%, #c9a462 40%, #101830 100%); border-radius: 110px 110px 0 0; }
  .call-block { right: 186px; top: 898px; text-align: right; }
  .call-label { font-size: 34px; color: var(--white); text-shadow: 2px 2px 0 var(--ink); }
  .call-number { font-family: "Michroma", sans-serif; font-size: 36px; color: var(--yellow); text-shadow: 2px 2px 0 var(--ink); margin-top: 4px; }
  .call-note { font-family: "Michroma", sans-serif; font-size: 17px; line-height: 26px; color: var(--white); margin-top: 6px; }

  /* footer */
  .footer-bar { left: 0; top: 1076px; width: 848px; height: 62px; background: linear-gradient(180deg, #07105a, var(--deep)); display: flex; align-items: center; justify-content: center; gap: 10px; font-family: "Michroma", sans-serif; font-size: 17px; color: var(--white); }
  .footer-bar .value { color: var(--yellow); }
  .bottom-tab { left: 110px; top: 1138px; width: 628px; height: 12px; background: var(--yellow); clip-path: polygon(0 0,100% 0,97% 100%,3% 100%); }
  .bottom-rail { left: 0; top: 1150px; width: 848px; height: 50px; background: linear-gradient(var(--steel), #d7d8dc); }
</style>
</head>
<body>
<main class="advert">
  <div class="abs top-rail"></div>
  <header class="abs header"></header>
  <div class="abs top-tab"></div>
  <div class="abs logo-word">LOGO</div>
  <div class="abs header-rule"></div>
  <div class="abs tagline">24/7 FULL COMPUTER SERVICE</div>
  <div class="abs header-band"></div>
  <div class="abs mid-rail"></div>

  <div class="abs tech-art" role="img" aria-label="Digital technology illustration with glowing data lines and code"></div>
  <section class="abs services-panel">
    <ul class="services">
      <li><span class="arrow">&gt;</span>Virus’s Removed</li>
      <li><span class="arrow">&gt;</span>Data Recovery</li>
      <li><span class="arrow">&gt;</span>Custom Computers<br>and Programs built</li>
      <li><span class="arrow">&gt;</span>Picked up &amp;<br>Dropped Off</li>
      <li><span class="arrow">&gt;</span>Private &amp; Business<br>Welcome</li>
    </ul>
  </section>
  <div class="abs laptop-art" role="img" aria-label="Silver laptop illustration"></div>
  <div class="abs laptop-small-art" role="img" aria-label="Small silver laptop illustration"></div>

  <div class="abs badge">ALL<br>COMPUTER<br>PROBLEMS<br>SOLVED</div>

  <section class="abs contact-strip"></section>
  <div class="abs hdd-art" role="img" aria-label="Photo of a hard disk drive being serviced"></div>
  <div class="abs receptionist-art" role="img" aria-label="Photo of a smiling receptionist wearing a headset"></div>
  <div class="abs call-block">
    <div class="call-label">CALL US ON:</div>
    <div class="call-number">0400 13 8562</div>
    <div class="call-note">where our friendly staff will<br>be pleased to assist you</div>
  </div>

  <footer class="abs footer-bar">
    <span>e:</span><span class="value">info@saltpancomputers.com.au</span>
    <span>•</span>
    <span>w:</span><span class="value">saltpancomputers.com.au</span>
  </footer>
  <div class="abs bottom-tab"></div>
  <div class="abs bottom-rail"></div>
</main>
</body>
</html>
```